Pricing Menu/Flyer for clothing manufacturer

We need a very nice looking and easy to understand flyer for our clothing manufacturing company.
There are packages that our customers can choose from to get their clothing of choice.

I have color coded the form so that you know exactly what I need.

- Keep " Clothing Brand Packages By Stichvora " as the top title of the flyer
- RED: The introduction of the flyer which should be placed at the top, not too big but big enough that its easy to read.
- BLUE: The main part of the flyer/menu. Should be big and bold. Use Bronze, silver, and platinum colors to make the package details look different. Format the details in a way that is easy for the customer to understand BUT PLEASE KEEP ALL DETAILS ACCURATE AND EXACTLY AS SAID ON THE FORM.
- GREEN: This is an extra section that does not have to be big and bold. Put it off on the bottom corner and make it big enough to read for our customer.

NOTE:
- Do not make the sections red blue and green, that is just for you to understand what I need to be done.
- Please do research on these type of flyers/menus before you start to create, so that you can do it best.
- The background does not need to be blank, make it look creative and nice to the eye.

PLEASE ASK ME ANY QUESTIONS IF YOU NEED TO. THANK YOU

```html
<!DOCTYPE html>
<html lang="en">
<head>
<meta charset="utf-8">
<title>Clothing Brand Packages By Stichvora</title>
<link href="https://fonts.googleapis.com/css2?family=Montserrat:wght@500;600;700;800&family=Open+Sans:wght@400;600;700&display=swap" rel="stylesheet">
<style>
:root{
  --orange:#f28c28;
  --orange-light:#f7a94f;
  --peach:#fde3c8;
  --ink:#2b2b2b;
  --grey-band:#58585a;
  --white:#ffffff;
  --stage:#e6e6e6;
}
*{box-sizing:border-box;margin:0;padding:0}
html,body{width:1200px;height:792px;overflow:hidden;background:var(--stage)}
body{font-family:"Open Sans",sans-serif;color:var(--ink)}
.flyer{position:absolute;left:330px;top:44px;width:540px;height:703px;background:var(--white);overflow:hidden;box-shadow:0 4px 18px rgba(0,0,0,.18)}
.header-art{position:absolute;left:0;top:0;width:540px;height:300px}
.title{position:absolute;left:24px;top:22px;color:var(--white);font-family:"Montserrat",sans-serif;font-weight:700;line-height:.98}
.title span{display:block}
.title .line-1{font-size:33px;letter-spacing:.5px}
.title .line-2{font-size:49px;font-weight:800}
.title .line-3{font-size:37px}
.title .byline{display:inline-block;margin:4px 0 0 105px;background:var(--white);color:var(--orange);font-size:12px;font-weight:700;padding:2px 14px 2px 10px;border-radius:3px}
.intro{position:absolute;left:150px;top:234px;width:380px;color:var(--white);font-size:9.5px;line-height:1.35;text-align:center;font-weight:600}
.slogan{position:absolute;left:0;top:292px;width:540px;height:34px;background:var(--peach);text-align:center;font-family:"Montserrat",sans-serif;font-weight:700;font-size:25px;line-height:34px;color:var(--ink)}
.goal{position:absolute;left:40px;top:336px;width:460px;text-align:center;color:var(--orange);font-size:10.5px;line-height:1.35;font-weight:600}
.card{position:absolute;width:138px;border:2px solid var(--orange);border-radius:9px;background:var(--white);overflow:hidden;display:flex;flex-direction:column;bottom:79px}
.card-1{left:44px;top:402px}
.card-2{left:201px;top:383px}
.card-3{left:356px;top:371px}
.card-head{background:var(--orange);color:var(--white);text-align:center;padding:4px 0 5px}
.price{font-family:"Montserrat",sans-serif;font-weight:800;font-size:21px;line-height:1.1}
.stars{font-size:7px;letter-spacing:3px;line-height:1.2}
.tier{font-size:9.5px;font-weight:600}
.card-body{flex:1;padding:5px 6px 0;font-size:7.6px;line-height:1.3}
.items{list-style:none}
.items li{position:relative;padding-left:13px;margin-bottom:4px;border-bottom:1px solid #eee;padding-bottom:2px}
.items li::before{content:"›";position:absolute;left:0;top:0;width:9px;height:9px;border:1px solid var(--orange);border-radius:50%;color:var(--orange);font-size:8px;line-height:7px;text-align:center;font-weight:700}
.items b{font-weight:700}
.size{text-align:center;margin-top:6px;font-size:6.8px;line-height:1.35}
.size .upto{font-size:8px;font-weight:600}
.card-foot{background:var(--peach);text-align:center;padding:3px 0 4px;border-top:2px solid var(--orange)}
.load{font-family:"Montserrat",sans-serif;font-weight:700;font-size:11px;color:var(--ink)}
.colours{font-size:8.5px;color:var(--orange);font-weight:600}
.addons{position:absolute;left:0;top:635px;width:540px;height:68px;background:var(--grey-band);padding:6px 22px 0}
.addons h3{font-family:"Montserrat",sans-serif;color:var(--orange);font-size:12px;font-weight:700}
.addon-cols{display:flex;justify-content:space-between;margin-top:1px}
.addon-cols ul{list-style:none}
.addon-cols li{color:var(--white);font-size:10px;line-height:1.45;display:flex;align-items:center;gap:4px}
.tick{width:11px;height:11px}
</style>
</head>
<body>
<main class="flyer">
  <svg class="header-art" viewBox="0 0 540 300" aria-hidden="true">
    <rect x="0" y="0" width="540" height="232" fill="#f28c28"/>
    <polygon points="420,0 540,0 540,70 360,232 260,232" fill="#f7a94f"/>
    <polygon points="490,0 540,0 540,20 400,150 370,150" fill="#f9b86a"/>
    <polygon points="0,198 330,198 540,90 540,118 345,222 0,222" fill="#ffffff"/>
    <polygon points="0,232 540,232 540,222 345,222 330,232" fill="#ffffff"/>
    <polygon points="0,222 60,222 110,290 0,290" fill="#ffffff"/>
    <polygon points="40,232 90,232 130,282 80,282" fill="#f28c28"/>
    <polygon points="128,232 540,232 540,286 150,286" fill="#f28c28"/>
  </svg>

  <h1 class="title">
    <span class="line-1">CLOTHING</span>
    <span class="line-2">BRAND</span>
    <span class="line-3">PACKAGE</span>
    <span class="byline">By Stichvora</span>
  </h1>

  <p class="intro">These packages are all base pricing, we understand every brand's is different. Content us to go over specific order details and Stichvora will do everything in our hands to accommodate your vision.</p>

  <h2 class="slogan">“Brick By Brick Brand Building”</h2>

  <p class="goal">Our goal is thoroughly assist you in either expanding, beginning, or accelerating your brand with your high quality embroidered garments.</p>

  <section class="card card-1">
    <div class="card-head">
      <div class="price">$500</div>
      <div class="stars">★☆☆☆☆</div>
      <div class="tier">Basic Tier Package</div>
    </div>
    <div class="card-body">
      <ul class="items">
        <li>15 Shirts</li>
        <li>10 Hoodies/Crewnecks</li>
      </ul>
      <div class="size" style="margin-top:38px">
        <div class="upto">Upto</div>
        4×4 inches<br>(1 Logo Placements)
      </div>
    </div>
    <div class="card-foot">
      <div class="load">“THE KIT” Load</div>
      <div class="colours">1-2 colour designs</div>
    </div>
  </section>

  <section class="card card-2">
    <div class="card-head">
      <div class="price">$1000</div>
      <div class="stars">★★☆☆☆</div>
      <div class="tier">Premuim Tier Package</div>
    </div>
    <div class="card-body">
      <ul class="items">
        <li>25 Shirts</li>
        <li><b>Option 1:</b><br>20 Hoodies or 20 Crewnecks</li>
        <li><b>Option 2:</b><br>Mix and Match 10 Hoodies &amp; 10 Crewnecks</li>
      </ul>
      <div class="size">
        <div class="upto">Upto</div>
        6×8 inches (1 Logo Placements)<br>Or<br>4×4 inches (2 Logo Placements - Left and Right Chest)
      </div>
    </div>
    <div class="card-foot">
      <div class="load">“HUSTLE” Load</div>
      <div class="colours">1-4 colour designs</div>
    </div>
  </section>

  <section class="card card-3">
    <div class="card-head">
      <div class="price">$2500</div>
      <div class="stars">★★★★★</div>
      <div class="tier">Executive Tier Package</div>
    </div>
    <div class="card-body">
      <ul class="items">
        <li>25 Shirts Sleeve Shirts</li>
        <li>25 Long Sleeve Shirts</li>
        <li>25 Hoodies</li>
        <li>25 Crewnecks</li>
      </ul>
      <div class="size">
        <div class="upto">Upto</div>
        8×10 inches (1 Logo Placements)<br>Or<br>4×4 inches (1 Logo Placements), 8×10 (1 Logo Placment “Back”)<br>Or<br>4×4 inches (2 Logo Placements “Left &amp; Right” Chest)
      </div>
    </div>
    <div class="card-foot">
      <div class="load">“SKYLINE” Load</div>
      <div class="colours">1-6 colour designs</div>
    </div>
  </section>

  <section class="addons">
    <h3>ADD ONS</h3>
    <div class="addon-cols">
      <ul>
        <li><svg class="tick" viewBox="0 0 12 12"><rect x="1" y="2" width="9" height="9" fill="none" stroke="#ffffff" stroke-width="1"/><path d="M3 6 L5.5 9 L11 1" fill="none" stroke="#f28c28" stroke-width="2"/></svg>Tags</li>
        <li><svg class="tick" viewBox="0 0 12 12"><rect x="1" y="2" width="9" height="9" fill="none" stroke="#ffffff" stroke-width="1"/><path d="M3 6 L5.5 9 L11 1" fill="none" stroke="#f28c28" stroke-width="2"/></svg>Extra Placement</li>
      </ul>
      <ul>
        <li><svg class="tick" viewBox="0 0 12 12"><rect x="1" y="2" width="9" height="9" fill="none" stroke="#ffffff" stroke-width="1"/><path d="M3 6 L5.5 9 L11 1" fill="none" stroke="#f28c28" stroke-width="2"/></svg>Custom Packaging</li>
        <li><svg class="tick" viewBox="0 0 12 12"><rect x="1" y="2" width="9" height="9" fill="none" stroke="#ffffff" stroke-width="1"/><path d="M3 6 L5.5 9 L11 1" fill="none" stroke="#f28c28" stroke-width="2"/></svg>Extra Logo</li>
      </ul>
      <ul>
        <li><svg class="tick" viewBox="0 0 12 12"><rect x="1" y="2" width="9" height="9" fill="none" stroke="#ffffff" stroke-width="1"/><path d="M3 6 L5.5 9 L11 1" fill="none" stroke="#f28c28" stroke-width="2"/></svg>Extra Colors On Design</li>
        <li><svg class="tick" viewBox="0 0 12 12"><rect x="1" y="2" width="9" height="9" fill="none" stroke="#ffffff" stroke-width="1"/><path d="M3 6 L5.5 9 L11 1" fill="none" stroke="#f28c28" stroke-width="2"/></svg>5-10 Additional Garments</li>
      </ul>
    </div>
  </section>
</main>
</body>
</html>
```